Feminine, flirty personal business Card Design

I need a new business card designed with my rebranded colors, personal pic and logo. It needs to be feminine without being girly. Since I work primarily virtually, address info can be omitted if it improves the design aesthetic. New tagline is "Your Partner in Success". Image from old biz card provided for information purposes only.

Target Market(s)

Online wellness/business coaches.

Industry/Entity Type

Business

Contact Information for Business Card

Tess Morvick, Head Technology Tamer
Email to use is tess@brookwaysvc.com
See image of old corporate style card for additional details

Font styles to use
Script

Requirements
Must have
• A fresh, feminine look and artistic aesthetic. Needs to appeal to my target demographic.
Nice to have
• Some type of embellishment to make it visually interesting.
Should not have
• Must not be linear and corporate looking.

```html
<!DOCTYPE html>
<html lang="en">
<head>
<meta charset="utf-8">
<title>Brookway Virtual Services – Business Card</title>
<link href="https://fonts.googleapis.com/css2?family=Roboto:wght@400;700&family=Great+Vibes&display=swap" rel="stylesheet">
<style>
  :root {
    --backdrop: #2b2b2d;
    --paper: #f7f7f7;
    --teal: #2bb3a3;
    --teal-light: #8fd8cf;
    --grey-text: #5b5b5b;
    --grey-line: #6d6d6d;
    --white: #ffffff;
  }
  * { box-sizing: border-box; margin: 0; padding: 0; }
  html, body {
    width: 1200px; height: 834px; overflow: hidden;
    background: var(--backdrop);
    font-family: "Roboto", Arial, sans-serif;
  }
  .stage {
    width: 1200px; height: 834px;
    display: flex; flex-direction: column; align-items: center; justify-content: center;
    gap: 40px;
  }
  .card {
    position: relative; width: 620px; height: 354px;
    background: linear-gradient(135deg, #ffffff 0%, var(--paper) 100%);
    overflow: hidden;
  }
  .card-front {
    display: flex; flex-direction: column; align-items: center; justify-content: center;
    gap: 6px;
  }
  .brand-name {
    font-weight: 700; color: var(--grey-text); letter-spacing: 1px;
    font-size: 52px; line-height: 1;
  }
  .tagline {
    font-family: "Great Vibes", cursive;
    color: var(--teal); font-size: 30px; line-height: 1.2;
  }
  .card-back .brand-name {
    position: absolute; left: 40px; top: 44px; font-size: 30px;
  }
  .contact {
    position: absolute; left: 40px; top: 104px;
    color: var(--grey-text); font-size: 11.5px; line-height: 15px;
  }
  .contact-list { list-style: none; margin-top: 12px; }
  .contact-list li { display: flex; align-items: center; gap: 8px; height: 15px; }
  .contact-list svg { width: 10px; height: 10px; fill: none; stroke: var(--teal); stroke-width: 1.6; }
  .portrait {
    position: absolute; left: 360px; top: 0; width: 240px; height: 300px;
    background: linear-gradient(160deg, #e9d2b8 0%, #b8d9d0 60%, #7fcfc3 100%);
  }
  .waves { position: absolute; inset: 0; width: 620px; height: 354px; }
  .person {
    position: absolute; right: 30px; top: 250px; text-align: right; color: var(--white);
  }
  .person-name {
    font-family: "Great Vibes", cursive;
    font-size: 30px; line-height: 1;
  }
  .person-role { font-size: 11px; margin-top: 4px; }
</style>
</head>
<body>
<main class="stage">
  <section class="card card-front">
    <div class="brand-name">BROOKWAY</div>
    <p class="tagline">Your Partner in Success</p>
  </section>

  <section class="card card-back">
    <div class="portrait" role="img" aria-label="Portrait photo of the card owner"></div>
    <svg class="waves" viewBox="0 0 620 354" aria-hidden="true">
      <path d="M230 306 C380 290 500 230 620 172" stroke="var(--grey-line)" stroke-width="5" fill="none"/>
      <path d="M0 300 C200 330 440 290 620 186 L620 354 L0 354Z" fill="var(--teal-light)"/>
      <path d="M0 314 C220 336 450 300 620 200 L620 354 L0 354Z" fill="var(--teal)"/>
    </svg>
    <div class="brand-name">BROOKWAY</div>
    <div class="contact">
      <p>Brookway Virtual Services</p>
      <p>2417 Alder Hollow Lane NE</p>
      <p>Marlow, Washington 98012 USA</p>
      <ul class="contact-list">
        <li><svg viewBox="0 0 10 10"><path d="M2 1 L4 1 L4.5 3 L3 4 C3.6 5.5 4.6 6.5 6 7 L7 5.5 L9 6 L9 8 C5 9 1 5 2 1Z"/></svg>555.014.2286</li>
        <li><svg viewBox="0 0 10 10"><rect x="2.5" y="0.8" width="5" height="8.4" rx="1"/></svg>555.017.4410</li>
        <li><svg viewBox="0 0 10 10"><rect x="0.8" y="2" width="8.4" height="6"/><path d="M0.8 2 L5 5.5 L9.2 2"/></svg>tess@brookwaysvc.com</li>
        <li><svg viewBox="0 0 10 10"><circle cx="5" cy="5" r="4.2"/><path d="M0.8 5 H9.2 M5 0.8 C2.5 3.5 2.5 6.5 5 9.2 M5 0.8 C7.5 3.5 7.5 6.5 5 9.2"/></svg>www.brookwaysvc.com</li>
      </ul>
    </div>
    <div class="person">
      <p class="person-name">Tess Morvick</p>
      <p class="person-role">Head Technology Tamer</p>
    </div>
  </section>
</main>
</body>
</html>
```